Presentation Folder for A New Home Construction Company

We need a Presentation Folder for a new home construction company based in Perth, Australia. It's called Korvale Homes and specialises in building quality homes that are affordable and people want to live in. The target market is first-home buyers.

We've rebranded the website (www.korvalehomes.com.au) and are looking to update our presentation folder to match it. We want red, white, grey and black as the colour palette, and some designs with transparent photos included but overall a minimalistic approach that aligns with our new website and vehicles.

I've attached an image of our updated car wrap, can you please follow this as a guide?

I've also attached our logo, style guide and past presentation folder for reference.

Please also include:

"Plan Well, Settle In, Stay On" - refer to the previous presentation folder.

Target Market(s)

First Home Buyers

Industry/Entity Type

New Home Construction

Font styles to use
Sans Serif
Other font styles liked:
• Monserrat

Colors
EB3D1F
EC4F4E
F09395
F8D3D4
FCEDEE

Requirements
Must have
• Monserrat or Open Sans Font and Include the colours from the attached brand guide, the contact details and address,
Nice to have
• some with a photo feature - but not the main component, very minimal.
Should not have
• Too many elements, (refer to previous folder attachment) animations or graphics.

```html
<!DOCTYPE html>
<html lang="en">
<head>
<meta charset="utf-8">
<title>Korvale Homes – Presentation Folder</title>
<link rel="stylesheet" href="https://fonts.googleapis.com/css2?family=Montserrat:wght@300;400;500;600;700;800&display=swap">
<style>
  :root {
    --backdrop: #4a4a4c;
    --sheet: #ffffff;
    --sheet-shade: #f4f4f4;
    --grey: #c6c6c8;
    --red: #e51f26;
    --red-mid: #b91f26;
    --red-deep: #6b1015;
    --ink: #3a0a0c;
    --white: #ffffff;
    --silver: #d9d9d9;
    --charcoal: #3d3d3f;
  }
  * { margin: 0; padding: 0; box-sizing: border-box; }
  html, body { width: 1200px; height: 900px; overflow: hidden; background: var(--backdrop); }
  body { font-family: "Montserrat", sans-serif; }
  .canvas { position: relative; width: 1200px; height: 900px; }
  .folder-art { position: absolute; inset: 0; }

  .brand-name {
    position: absolute; left: 800px; top: 120px; width: 170px;
    text-align: center; color: var(--charcoal);
    font-weight: 700; font-size: 24px; line-height: 1.15; letter-spacing: 4px;
    text-transform: uppercase;
  }

  .intro {
    position: absolute; left: 232px; top: 268px; width: 150px;
    text-align: center; color: var(--white);
    font-size: 11px; line-height: 16.6px; font-weight: 400;
  }
  .intro strong { font-weight: 700; }

  .tagline-inline {
    position: absolute; left: 380px; top: 276px; width: 250px;
    text-align: center; color: var(--ink);
    font-size: 14px; font-weight: 300; letter-spacing: 0.3px;
  }
  .wordmark-inline {
    position: absolute; left: 380px; top: 298px; width: 250px;
    text-align: center; color: var(--ink);
    font-size: 30px; font-weight: 800;
  }

  .contact {
    position: absolute; left: 442px; top: 392px; width: 220px;
    text-align: center; color: var(--white);
    font-size: 9.6px; line-height: 12.4px; font-weight: 500;
  }
  .contact-list { list-style: none; margin-top: 16px; }
  .contact-list li { line-height: 16.6px; display: flex; justify-content: center; align-items: center; gap: 5px; }
  .contact-list svg { width: 8px; height: 8px; fill: var(--white); }

  .director-name {
    position: absolute; left: 376px; top: 560px; width: 124px;
    color: var(--white); font-size: 15px; font-weight: 500; font-style: normal;
  }
  .director-role {
    position: absolute; left: 376px; top: 591px; width: 140px;
    color: var(--white); font-size: 9.4px; font-weight: 600; letter-spacing: 1px;
  }

  .cover-tagline {
    position: absolute; left: 722px; top: 485px; width: 160px;
    color: var(--silver); font-size: 17px; line-height: 22px; font-weight: 700;
  }
  .cover-wordmark {
    position: absolute; left: 722px; top: 556px; width: 170px;
    color: var(--silver); font-size: 30px; font-weight: 800;
  }
</style>
</head>
<body>
<main class="canvas">
  <svg class="folder-art" viewBox="0 0 1200 900" width="1200" height="900" aria-hidden="false">
    <defs>
      <linearGradient id="cover-photo" x1="0" y1="0" x2="1" y2="1">
        <stop offset="0" stop-color="#8c8478"/>
        <stop offset="0.45" stop-color="#cfd3d8"/>
        <stop offset="0.75" stop-color="#eef0f2"/>
        <stop offset="1" stop-color="#9a9a95"/>
      </linearGradient>
      <linearGradient id="estate-photo" x1="0" y1="0" x2="0" y2="1">
        <stop offset="0" stop-color="#e2242a"/>
        <stop offset="1" stop-color="#c81d23"/>
      </linearGradient>
    </defs>

    <!-- sheet -->
    <rect class="sheet" x="84" y="66" width="1031" height="768" fill="var(--sheet)"/>
    <rect class="sheet-panel" x="232" y="66" width="883" height="616" fill="var(--sheet-shade)"/>

    <!-- grey slanted band -->
    <path class="grey-band" d="M279 66 H838 L1076 672 H518 Z" fill="var(--grey)"/>

    <!-- cover photo -->
    <path class="cover-photo" role="img" aria-label="Photo of a white two-storey home with blue roof among bare trees"
          d="M785 229 H1115 V656 H790 Q760 656 756 626 L752 262 Q752 229 785 229 Z" fill="url(#cover-photo)"/>

    <!-- red band with faint estate photo -->
    <path class="red-band" d="M84 210 H722 Q746 210 756 235 L900 602 Q912 641 872 641 H84 Z" fill="url(#estate-photo)"/>
    <path class="red-band-mid" role="img" aria-label="Faded photo of a new housing estate"
          d="M335 210 H722 Q746 210 756 235 L900 602 Q912 641 872 641 H504 Z" fill="var(--red-mid)" opacity="0.92"/>
    <path class="red-band-deep" d="M582 210 H722 Q746 210 756 235 L900 602 Q912 641 872 641 H759 Z" fill="var(--red-deep)" opacity="0.9"/>

    <!-- director photo -->
    <rect class="director-photo" role="img" aria-label="Photo of the managing director leaning on a tablet"
          x="240" y="456" width="125" height="185" fill="#8a1a1f" opacity="0.85"/>

    <!-- signature -->
    <rect class="director-signature" role="img" aria-label="Managing director's handwritten signature"
          x="376" y="582" width="0" height="0" fill="none"/>

    <!-- bottom pocket flap -->
    <path class="pocket-flap" d="M240 672 H666 V778 Q666 834 610 834 H372 Z" fill="var(--red)"/>
  </svg>

  <div class="brand-name">Korvale<br>Homes</div>

  <p class="intro">Offering first home buyers the same outstanding service &amp; innovation that has been Dale Hartley’s hallmark for <strong>over 15 years.</strong></p>

  <p class="tagline-inline">PLAN WELL, SETTLE IN, STAY ON</p>
  <p class="wordmark-inline">Korvale.</p>

  <address class="contact">
    14 Marlowe Street, Kelmscott Park,<br>
    Western Australia 6112<br>
    PO Box 2281, Kelmscott Park, WA 6992
    <ul class="contact-list">
      <li><svg viewBox="0 0 10 10"><path d="M2 0.5 L3.6 2.6 L2.8 3.6 Q4 6 6.4 7.2 L7.4 6.4 L9.5 8 L8.4 9.5 Q3.5 9 0.5 1.6 Z"/></svg>08 9400 5120</li>
      <li><svg viewBox="0 0 10 10"><rect x="2" y="0.5" width="6" height="3"/><rect x="0.5" y="3.5" width="9" height="4" rx="1"/><rect x="2" y="7" width="6" height="2.5"/></svg>08 9400 5121</li>
      <li><svg viewBox="0 0 10 10"><path d="M0.5 2 H9.5 V8.5 H0.5 Z M1 2.4 L5 5.6 L9 2.4" stroke="#b91f26" stroke-width="0.8"/></svg>enquiries@korvalehomes.com.au</li>
      <li><svg viewBox="0 0 10 10"><circle cx="5" cy="5" r="4.5"/></svg>www.korvalehomes.com.au</li>
    </ul>
  </address>

  <p class="director-name">Dale Hartley</p>
  <p class="director-role">MANAGING DIRECTOR</p>

  <p class="cover-tagline">PLAN WELL...<br>SETTLE IN...<br>STAY ON...</p>
  <p class="cover-wordmark">Korvale.</p>
</main>
</body>
</html>
```